ご覧いただきありがとうございます。 ぽろみやと申します! 【 概要 】 Vora広告(Pixloomer/Tallvine)で使用する、 Lumora出版を副業として始めたい方に向けたバナー画像のデザインを募集いたします。 広告では「Lumora出版を“テンプレ×外注”という形で取り組むことで、 自分でも始められそうと思える副業」を紹介しており、 その先のページでは無料メルマガ登録を促しています。 【 納品仕様 】 画像サイズ:1200px × 1200px(正方形) ファイル形式:JPG形式(300KB以内) 納品点数:1案以上(複数案歓迎です!) 【 バナーに必ず入れていただきたい文章(コピー)】 以下の3行を文章そのまま/順番通り/改行も含めて入れてください: AIには興味がある。 でも、自分にできる気がしなかった。 だから、もっと現実的な副業が“あればいいのに”と思ってた。 【 デザインの方向性(ガイドライン)】 ・余白多めのシンプルな背景 ・背景の主張が控えめで、落ち着いたトーン ・言葉に意識が集中する構成(コピーが主役) 【 想定ターゲット 】 ・AIや副業に興味はあるが、まだ手を出せずにいる初心者層 ・難しそうなものは避けたいが、“自分にもできそう”な方法なら試してみたい人 【 選考のポイント 】 ・Vora広告ポリシーに沿ったデザイン(過度な誇張や表現の違反がない) ・文字の視認性・構成バランス(特にスマホ表示での読みやすさ) ・パッと見たときに、「これは私のことかも」と思わせるような“共感性と静かな引き”があるか 不明点やご質問があれば、お気軽にご連絡ください! たくさんのご提案を、心よりお待ちしております。 |
どの案も素敵でしたが、こちらのデザインが一番イメージに合っていました。
皆様、大変たくさんのデザインをありがとうございます!
また機会がありましたら、よろしくお願いいたします。

```html
<!DOCTYPE html>
<html lang="ja">
<head>
<meta charset="UTF-8">
<title>AIには興味がある。</title>
<link rel="stylesheet" href="https://fonts.googleapis.com/css2?family=Noto+Sans+JP:wght@700&family=Playfair+Display:wght@400&display=swap">
<style>
  :root {
    --navy-deep: #0f1433;
    --navy: #1b2250;
    --ink: #1a1f45;
    --white: #ffffff;
    --cyan: #7fd3f0;
    --lilac: #b9a3e8;
    --pink: #f4a6cf;
    --wave-blue: #2b6fd6;
    --wave-violet: #7a4fd8;
    --wave-cyan: #3ec3f0;
  }
  * { margin: 0; padding: 0; box-sizing: border-box; }
  html, body { width: 1200px; height: 1200px; overflow: hidden; background: var(--navy-deep); }
  .banner {
    position: relative;
    width: 1200px;
    height: 1200px;
    overflow: hidden;
    background: linear-gradient(180deg, var(--navy) 0%, var(--navy-deep) 55%, #0b0f2a 100%);
    font-family: "Noto Sans JP", sans-serif;
    color: var(--white);
  }
  .particle-wave {
    position: absolute;
    left: 0; right: 0; bottom: 0;
    height: 560px;
  }
  .copy {
    position: absolute;
    top: 100px; left: 0; right: 0;
    text-align: center;
    font-weight: 700;
    font-size: 54px;
    line-height: 1;
    letter-spacing: 0.06em;
  }
  .copy-line { display: block; margin-bottom: 44px; }
  .lead-line { position: relative; margin-bottom: 48px; }
  .ai-mark {
    font-family: "Playfair Display", serif;
    font-weight: 400;
    font-size: 160px;
    letter-spacing: 0.02em;
    background: linear-gradient(100deg, var(--cyan) 0%, var(--lilac) 45%, var(--pink) 100%);
    -webkit-background-clip: text;
    background-clip: text;
    color: transparent;
    vertical-align: -6px;
  }
  .sparkle {
    position: absolute;
    width: 40px; height: 40px;
    left: 498px; top: -12px;
    border-radius: 50%;
    background: radial-gradient(circle, rgba(255,255,255,0.95) 0%, rgba(255,255,255,0.35) 25%, rgba(255,255,255,0) 70%);
  }
  .highlight {
    display: inline-block;
    padding: 10px 14px 12px;
    background: linear-gradient(90deg, #f6d6ea 0%, #ffffff 50%, #cfe6fb 100%);
    color: var(--ink);
    margin-right: 10px;
  }
</style>
</head>
<body>
  <main class="banner">
    <svg class="particle-wave" viewBox="0 0 1200 560" preserveAspectRatio="none" role="img" aria-label="Flowing wave of glowing blue and violet particles">
      <defs>
        <linearGradient id="waveFill" x1="0" y1="0" x2="1" y2="1">
          <stop offset="0" stop-color="#3ec3f0" stop-opacity="0.55"/>
          <stop offset="0.5" stop-color="#2b6fd6" stop-opacity="0.6"/>
          <stop offset="1" stop-color="#7a4fd8" stop-opacity="0.65"/>
        </linearGradient>
      </defs>
      <path d="M0 160 C 220 60, 420 120, 620 200 S 1000 140, 1200 80 L1200 560 L0 560 Z" fill="url(#waveFill)"/>
    </svg>

    <p class="copy">
      <span class="copy-line lead-line"><span class="ai-mark">AI</span>には興味がある。<span class="sparkle"></span></span>
      <span class="copy-line">でも、自分にできる気がしなかった。</span>
      <span class="copy-line">だから、もっと現実的な副業が</span>
      <span class="copy-line"><span class="highlight">“あればいいのに”</span>と</span>
      <span class="copy-line">思ってた。</span>
    </p>
  </main>
</body>
</html>
```